Letterhead

We are looking for a basic letterhead. It should include our logo, website - northpeakkitchenware.com, phone 907.418.3952, toll free 855.392.6180, and fax 907.418.5263, along with our address 4837 Birchwood Lane, Anchorage, AK 99517. I want something that will look good printed in color or black and white.

```html
<!DOCTYPE html>
<html lang="en">
<head>
<meta charset="utf-8">
<title>North Peak Kitchenware Letterhead</title>
<link href="https://fonts.googleapis.com/css2?family=Montserrat:wght@500;700;800&display=swap" rel="stylesheet">
<style>
  :root {
    --navy: #1f3a7a;
    --red: #c8394a;
    --paper: #ffffff;
    --backdrop: #e9e9ea;
  }
  html, body {
    margin: 0;
    padding: 0;
    width: 1200px;
    height: 1000px;
    overflow: hidden;
    background: var(--backdrop);
    font-family: "Montserrat", Arial, sans-serif;
  }
  .letterhead {
    position: absolute;
    left: 245px;
    top: 40px;
    width: 710px;
    height: 920px;
    background: var(--paper);
    box-shadow: 0 2px 10px rgba(0,0,0,0.08);
    overflow: hidden;
  }
  .brand {
    position: absolute;
    left: 48px;
    top: 64px;
    display: flex;
    align-items: center;
    gap: 10px;
  }
  .brand-mark {
    width: 14px;
    height: 14px;
    background: var(--navy);
  }
  .brand-name {
    font-weight: 800;
    font-size: 22px;
    color: var(--navy);
    letter-spacing: 0.5px;
    text-transform: uppercase;
  }
  .contact-list {
    position: absolute;
    right: 48px;
    top: 44px;
    list-style: none;
    margin: 0;
    padding: 0;
    font-size: 11px;
    font-weight: 500;
    color: var(--navy);
    line-height: 18px;
  }
  .contact-list li {
    display: flex;
    align-items: center;
    gap: 6px;
  }
  .contact-list svg { width: 11px; height: 11px; fill: var(--red); }
  .note { color: var(--red); font-size: 9px; }
  .footer-info {
    position: absolute;
    left: 20px;
    right: 180px;
    bottom: 30px;
    display: flex;
    justify-content: space-between;
    font-size: 11px;
    font-weight: 500;
    color: var(--navy);
  }
  .footer-info span {
    display: flex;
    align-items: center;
    gap: 6px;
  }
  .footer-info svg { width: 11px; height: 11px; fill: var(--red); }
  .footer-band {
    position: absolute;
    left: 0;
    bottom: 0;
    width: 710px;
    height: 80px;
  }
  .footer-band path { fill: var(--red); }
</style>
</head>
<body>
  <main class="letterhead">
    <div class="brand">
      <span class="brand-mark"></span>
      <span class="brand-name">North Peak Kitchenware</span>
    </div>

    <ul class="contact-list">
      <li>
        <svg viewBox="0 0 24 24"><path d="M6.6 10.8a15 15 0 0 0 6.6 6.6l2.2-2.2a1 1 0 0 1 1-.25 11.4 11.4 0 0 0 3.6.57 1 1 0 0 1 1 1V20a1 1 0 0 1-1 1A17 17 0 0 1 3 4a1 1 0 0 1 1-1h3.5a1 1 0 0 1 1 1c0 1.25.2 2.45.57 3.57a1 1 0 0 1-.25 1z"/></svg>
        907.418.3952
      </li>
      <li>
        <svg viewBox="0 0 24 24"><path d="M6.6 10.8a15 15 0 0 0 6.6 6.6l2.2-2.2a1 1 0 0 1 1-.25 11.4 11.4 0 0 0 3.6.57 1 1 0 0 1 1 1V20a1 1 0 0 1-1 1A17 17 0 0 1 3 4a1 1 0 0 1 1-1h3.5a1 1 0 0 1 1 1c0 1.25.2 2.45.57 3.57a1 1 0 0 1-.25 1z"/></svg>
        855.392.6180 <span class="note">(Toll Free)</span>
      </li>
      <li>
        <svg viewBox="0 0 24 24"><path d="M6 2h10v5H6zM4 8h16a2 2 0 0 1 2 2v7h-4v5H6v-5H2v-7a2 2 0 0 1 2-2zm4 9v3h8v-3z"/></svg>
        907.418.5263
      </li>
    </ul>

    <div class="footer-info">
      <span>
        <svg viewBox="0 0 24 24"><path d="M12 2a10 10 0 1 0 0 20 10 10 0 0 0 0-20zm0 2c1 0 2.4 2 3 5H9c.6-3 2-5 3-5zM4.3 9h2.8a17 17 0 0 0 0 6H4.3a8 8 0 0 1 0-6zm4.7 6a15 15 0 0 1 0-6h6a15 15 0 0 1 0 6zm.1 2h5.8c-.6 3-2 5-2.9 5s-2.3-2-2.9-5zm7.8-2a17 17 0 0 0 0-6h2.8a8 8 0 0 1 0 6z"/></svg>
        www.northpeakkitchenware.com
      </span>
      <span>
        <svg viewBox="0 0 24 24"><path d="M12 2a7 7 0 0 0-7 7c0 5.2 7 13 7 13s7-7.8 7-13a7 7 0 0 0-7-7zm0 9.5A2.5 2.5 0 1 1 12 6.5a2.5 2.5 0 0 1 0 5z"/></svg>
        4837 Birchwood Lane, Anchorage, AK 99517
      </span>
    </div>

    <svg class="footer-band" viewBox="0 0 710 80" preserveAspectRatio="none" aria-hidden="true">
      <path d="M0 80 L0 60 L548 60 L566 36 L588 36 L602 8 L690 8 L710 0 L710 80 Z"/>
    </svg>
  </main>
</body>
</html>
```